Quill And Ferry Business Card

I need a business card designed around my logo (which was designed here on Sketch Forum!)

Target Market(s)

Professional Businesses

Industry/Entity Type

Business

Requirements
Must have
• Details that must be on the business card:

Renata Ovalle
Director
0491 253 608
renata@quillandferry.com.au
www.quillandferry.com.au
PO Box 4720 Fitzroy North Vic 3068

```html
<!DOCTYPE html>
<html lang="en">
<head>
<meta charset="utf-8">
<title>Quill And Ferry Business Card</title>
<link rel="stylesheet" href="https://fonts.googleapis.com/css2?family=Cinzel:wght@400;600&family=Questrial&display=swap">
<style>
  :root {
    --brand-red: #c8202a;
    --brand-red-deep: #b81b24;
    --ink: #2b2b2b;
    --paper: #ffffff;
    --backdrop: #ece9e6;
  }
  * { box-sizing: border-box; margin: 0; padding: 0; }
  html, body {
    width: 1200px;
    height: 1000px;
    overflow: hidden;
    background: var(--backdrop);
  }
  .canvas {
    position: relative;
    width: 1200px;
    height: 1000px;
  }
  .card {
    position: absolute;
    width: 312px;
    height: 522px;
    box-shadow: 0 6px 18px rgba(0,0,0,0.18);
    text-align: center;
  }
  /* Front */
  .card--front {
    left: 110px;
    top: 25px;
    background: linear-gradient(160deg, var(--brand-red) 0%, var(--brand-red-deep) 100%);
    color: var(--paper);
  }
  .wordmark {
    position: absolute;
    left: 0; right: 0;
    display: flex;
    align-items: center;
    justify-content: center;
    gap: 10px;
    font-family: "Cinzel", serif;
    font-weight: 600;
    letter-spacing: 0.02em;
  }
  .card--front .wordmark {
    top: 318px;
    font-size: 26px;
    color: var(--paper);
  }
  .wordmark__square {
    width: 14px;
    height: 14px;
    background: currentColor;
  }
  .card--front .site {
    position: absolute;
    left: 0; right: 0;
    top: 478px;
    font-family: "Cinzel", serif;
    font-size: 11px;
    letter-spacing: 0.06em;
  }
  /* Back */
  .card--back {
    left: 770px;
    top: 60px;
    background: var(--paper);
    color: var(--brand-red);
  }
  .card--back .wordmark {
    top: 168px;
    font-size: 24px;
    color: var(--ink);
  }
  .person {
    position: absolute;
    left: 0; right: 0;
    top: 332px;
    font-family: "Questrial", sans-serif;
  }
  .person__name {
    font-size: 25px;
    color: var(--brand-red);
    line-height: 1.1;
  }
  .person__role {
    font-size: 12px;
    letter-spacing: 0.38em;
    color: var(--ink);
    margin-top: 2px;
  }
  .contact {
    position: absolute;
    left: 0; right: 0;
    top: 402px;
    font-family: "Questrial", sans-serif;
    font-size: 12px;
    line-height: 19.5px;
    color: var(--brand-red);
    list-style: none;
  }
</style>
</head>
<body>
  <main class="canvas">
    <section class="card card--front" aria-label="Business card front">
      <div class="wordmark"><span class="wordmark__square"></span><span>Quill And Ferry</span></div>
      <p class="site">WWW.QUILLANDFERRY.COM.AU</p>
    </section>

    <section class="card card--back" aria-label="Business card back">
      <div class="wordmark"><span class="wordmark__square" style="background: var(--brand-red);"></span><span>Quill And Ferry</span></div>
      <div class="person">
        <p class="person__name">Renata Ovalle</p>
        <p class="person__role">DIRECTOR</p>
      </div>
      <ul class="contact">
        <li>0491 253 608</li>
        <li>renata@quillandferry.com.au</li>
        <li>www.quillandferry.com.au</li>
        <li>PO Box 4720 Fitzroy North Vic 3068</li>
      </ul>
    </section>
  </main>
</body>
</html>
```